BLUE HAVEN (Business Card for Training Company)

Blue Haven is a training and consultancy company with a focus on executive protection and medical. I would like the card to be nice and sharp, not overdone and in black and red. I would also like it to highlight that it is "A Dravin Company"

I would like it to be simple and highlight a few things.

1. Name
2. Title
3. Phone Number
4. Email

I would also like www.dravinholdings.example/blue-haven to be on the card somewhere.

Target Market(s)

Security Companies

Industry/Entity Type

Security

Contact Information for Business Card

Blue Haven is a training and consultancy company with a focus on executive protection and medical. I would like the card to be nice and sharp, not overdone and in black and red. I would also like it to highlight that it is "A Dravin Company" I would like it to be simple and highlight a few things. 1. Name 2. Title 3. Phone Number 4. Email I would also like www.dravinholdings.example/blue-haven to be on the card somewhere.

Requirements
Must have
• A Dravin Company listed on the card and the website
Nice to have
• Highlight Medical Training, Consultancy & Executive Protection Courses

```html
<!DOCTYPE html>
<html lang="en">
<head>
<meta charset="utf-8">
<title>Blue Haven — Business Card</title>
<link rel="stylesheet" href="https://fonts.googleapis.com/css2?family=Montserrat:wght@400;500;600;700;800&display=swap">
<style>
  :root {
    --brand-red: #6e0a0c;
    --frame-red: #7a1214;
    --ink: #141414;
    --paper: #ffffff;
    --backdrop: #9a9a9a;
  }
  * { box-sizing: border-box; margin: 0; padding: 0; }
  html, body { width: 1200px; height: 1200px; overflow: hidden; }
  body {
    background: var(--backdrop);
    font-family: "Montserrat", Arial, sans-serif;
    display: flex;
    align-items: center;
    justify-content: center;
    gap: 40px;
  }
  .card {
    position: relative;
    width: 540px;
    height: 310px;
    background: var(--paper);
    box-shadow: 0 18px 40px rgba(0,0,0,0.28);
    overflow: hidden;
  }

  /* Front */
  .card-front .frame {
    position: absolute;
    inset: 0;
    width: 100%;
    height: 100%;
  }
  .card-front .wordmark {
    position: absolute;
    left: 70px;
    top: 62px;
    color: var(--ink);
    font-weight: 800;
    font-size: 54px;
    line-height: 56px;
    letter-spacing: 1px;
  }
  .card-front .rule {
    position: absolute;
    left: 58px;
    top: 195px;
    width: 398px;
    height: 5px;
    background: var(--brand-red);
  }
  .card-front .parent-company {
    position: absolute;
    left: 72px;
    top: 208px;
    color: var(--brand-red);
    font-weight: 700;
    font-size: 20px;
    letter-spacing: 0.3px;
  }
  .card-front .web {
    position: absolute;
    left: 72px;
    top: 234px;
    color: var(--brand-red);
    font-size: 9.5px;
    letter-spacing: 0.8px;
  }

  /* Back */
  .card-back .wordmark {
    position: absolute;
    left: 37px;
    top: 22px;
    color: var(--ink);
    font-weight: 800;
    font-size: 18px;
    line-height: 20px;
    letter-spacing: 0.5px;
  }
  .card-back .person-name {
    position: absolute;
    left: 37px;
    top: 112px;
    color: var(--brand-red);
    font-weight: 500;
    font-size: 36px;
    line-height: 42px;
    white-space: nowrap;
  }
  .card-back .person-title {
    position: absolute;
    left: 41px;
    top: 159px;
    color: var(--brand-red);
    font-weight: 500;
    font-size: 11px;
    letter-spacing: 0.4px;
  }
  .card-back .contact {
    position: absolute;
    left: 41px;
    top: 186px;
    list-style: none;
    color: var(--brand-red);
    font-size: 15px;
    line-height: 21px;
  }
  .card-back .contact strong { font-weight: 600; }
  .card-back .art {
    position: absolute;
    left: 335px;
    top: 124px;
    width: 205px;
    height: 108px;
    background: linear-gradient(180deg, var(--brand-red) 0 19%, transparent 19% 36%, var(--brand-red) 36% 100%);
  }
</style>
</head>
<body>
  <section class="card card-front">
    <svg class="frame" viewBox="0 0 540 310" aria-hidden="true">
      <path d="M14 13 H526 V262 A36 36 0 0 1 490 298 H14 Z" fill="none" stroke="var(--frame-red)" stroke-width="2.5"/>
      <path d="M526 262 A36 36 0 0 1 490 298 H526 Z" fill="var(--frame-red)"/>
    </svg>
    <div class="wordmark">BLUE<br>HAVEN</div>
    <div class="rule" aria-hidden="true"></div>
    <p class="parent-company">A DRAVIN COMPANY</p>
    <p class="web">www.dravinholdings.example/blue-haven</p>
  </section>

  <section class="card card-back">
    <div class="wordmark">BLUE<br>HAVEN</div>
    <h1 class="person-name">JORDAN VALE</h1>
    <p class="person-title">Certified Firearm Specialist</p>
    <ul class="contact">
      <li>Office: (555) 010-2040</li>
      <li>Mobile: <strong>(555) 010-3131</strong></li>
      <li>Email: jordan@bluehaven.example</li>
    </ul>
    <div class="art" role="img" aria-label="Illustration of two bullets pointing left"></div>
  </section>
</body>
</html>
```